Home Staging Company needs business card design

We're a home staging company called Brightly Settled Home Staging. We would like a business card design that includes aqua and gray. Our current logo of house within chair is fine but I find we almost always use the logo in one color. I'll upload images of front and back of our current card and our logo. Note that we have dropped "Solutions" from our company name and don't want to include it on the card.

Target Market(s)

Realtors and homeowners - people interested in selling their homes

Contact Information for Business Card

Marisol Vantrease
Brightly Settled Home Staging
612-348-9071
www.brightlysettled.example
marisol@brightlysettled.example

Font styles to use
Serif
Script

Requirements
Must have
• My logo and contact details
• UPDATE***
• I forgot to say that the company name should be included on the front of the card somehow.

```html
<!DOCTYPE html>
<html lang="en">
<head>
<meta charset="utf-8">
<title>Brightly Settled Home Staging – Business Card</title>
<link rel="stylesheet" href="https://fonts.googleapis.com/css2?family=Playfair+Display:wght@400&family=Roboto:wght@400&family=Poppins:wght@300&display=swap">
<style>
  :root {
    --backdrop: #bdbdbd;
    --aqua-top: #4fb0ba;
    --aqua-bottom: #1a86ab;
    --aqua-flat: #4eabb3;
    --aqua-deep: #1f8fae;
    --slate: #3a3f42;
    --paper: #f4f4f2;
    --white: #ffffff;
    --soft-white: rgba(255,255,255,0.9);
  }
  * { margin: 0; padding: 0; box-sizing: border-box; }
  html, body {
    width: 1200px; height: 576px; overflow: hidden;
    background: var(--backdrop);
  }
  .canvas { position: relative; width: 1200px; height: 576px; }

  .card {
    position: absolute; top: 138px;
    border-radius: 14px; overflow: hidden;
  }

  /* Front */
  .card-front {
    left: 82px; width: 485px; height: 294px;
    background: linear-gradient(180deg, var(--aqua-top) 0%, var(--aqua-bottom) 100%);
    color: var(--white);
  }
  .front-wordmark {
    position: absolute; left: 0; right: 0; top: 108px;
    text-align: center;
    font-family: "Playfair Display", Georgia, serif;
    font-weight: 400;
    color: var(--white);
  }
  .front-wordmark .wordmark-name {
    display: block; font-size: 38px; line-height: 1.15;
  }
  .front-wordmark .wordmark-tag {
    display: block; margin-top: 6px;
    font-size: 15px; letter-spacing: 9px; padding-left: 9px;
    text-transform: uppercase; line-height: 1.2;
  }
  .front-web {
    position: absolute; left: 0; right: 0; top: 268px;
    text-align: center;
    font-family: "Poppins", Arial, sans-serif;
    font-weight: 300; font-size: 12.5px;
    color: var(--soft-white);
  }

  /* Back */
  .card-back {
    left: 602px; width: 481px; height: 291px;
    background: var(--aqua-flat);
    color: var(--white);
  }
  .back-shape { position: absolute; inset: 0; }
  .person-name {
    position: absolute; left: 26px; top: 30px;
    font-family: "Roboto", Arial, sans-serif;
    font-weight: 400; font-size: 19px;
  }
  .person-title {
    position: absolute; left: 26px; top: 59px;
    font-family: "Poppins", Arial, sans-serif;
    font-weight: 300; font-size: 10.5px;
  }
  .contact-list {
    position: absolute; left: 26px; top: 205px;
    list-style: none;
    font-family: "Poppins", Arial, sans-serif;
    font-weight: 300; font-size: 12px;
  }
  .contact-list li {
    display: flex; align-items: center; height: 17.5px;
  }
  .contact-icon { width: 11px; height: 11px; margin-right: 11px; flex: none; }

  .brand-mark {
    position: absolute; left: 312px; top: 100px;
    width: 80px; height: 80px; border-radius: 50%;
    background: var(--aqua-deep);
  }
  .brand-lockup {
    position: absolute; left: 410px; top: 44px; height: 204px;
    writing-mode: vertical-rl;
    transform: rotate(180deg);
    text-align: center;
    font-family: "Playfair Display", Georgia, serif;
    font-weight: 400;
    color: var(--slate);
    white-space: nowrap;
  }
  .brand-lockup .lockup-name {
    display: block; font-size: 21px; line-height: 1.3;
  }
  .brand-lockup .lockup-tag {
    display: block; margin-right: 4px;
    font-size: 10.5px; letter-spacing: 6px;
    text-transform: uppercase; line-height: 1.3;
  }
</style>
</head>
<body>
<main class="canvas">

  <section class="card card-front" aria-label="Card front">
    <p class="front-wordmark">
      <span class="wordmark-name">Brightly Settled</span>
      <span class="wordmark-tag">Home Staging</span>
    </p>
    <p class="front-web">www.brightlysettled.example</p>
  </section>

  <section class="card card-back" aria-label="Card back">
    <svg class="back-shape" width="481" height="291" viewBox="0 0 481 291" aria-hidden="true">
      <path d="M310 0 Q246 145.5 310 291 L481 291 L481 0 Z" fill="var(--paper)"/>
      <path d="M304 -2 Q240 145.5 310 293" fill="none" stroke="var(--slate)" stroke-width="7"/>
    </svg>

    <h1 class="person-name">Marisol Vantrease</h1>
    <p class="person-title">Managing Director</p>

    <ul class="contact-list">
      <li>
        <svg class="contact-icon" viewBox="0 0 12 12" aria-hidden="true">
          <path d="M1 4 Q6 0 11 4 L10 5.5 L8 4.5 L8 3.5 Q6 3 4 3.5 L4 4.5 L2 5.5 Z M3 6 L9 6 L10 11 L2 11 Z" fill="var(--white)"/>
        </svg>
        612-348-9071
      </li>
      <li>
        <svg class="contact-icon" viewBox="0 0 12 12" aria-hidden="true">
          <g fill="none" stroke="var(--white)" stroke-width="1">
            <circle cx="6" cy="6" r="5"/>
            <ellipse cx="6" cy="6" rx="2.2" ry="5"/>
            <line x1="1" y1="6" x2="11" y2="6"/>
          </g>
        </svg>
        www.brightlysettled.example
      </li>
      <li>
        <svg class="contact-icon" viewBox="0 0 12 12" aria-hidden="true">
          <rect x="0.5" y="2" width="11" height="8" fill="var(--white)"/>
          <path d="M0.5 2 L6 6.5 L11.5 2" fill="none" stroke="var(--aqua-flat)" stroke-width="1"/>
        </svg>
        marisol@brightlysettled.example
      </li>
    </ul>

    <span class="brand-mark" aria-hidden="true"></span>
    <p class="brand-lockup">
      <span class="lockup-name">Brightly Settled</span>
      <span class="lockup-tag">Home Staging</span>
    </p>
  </section>

</main>
</body>
</html>
```